PPT Template for an investment fund to use in their pitchbooks

Our firm is an international investment fund and are seeking a PPT template to use in our pitch book (and subsequent PPTs). We would need a template for a title slide and then subsequent text/info slides. A clean & uncluttered feel is preferred as well as no watermark on slides. Please see our logo attached. The logo color code is #19478d. Font is Gotham-Medium.

Target Market(s)

Sophisticated investors

Industry/Entity Type

Finance

Colors
ffffff
0356a4

```html
<!DOCTYPE html>
<html lang="en">
<head>
<meta charset="utf-8">
<title>Harbourline Capital – Pitchbook Template</title>
<link href="https://fonts.googleapis.com/css2?family=Montserrat:wght@400;500;600;700&display=swap" rel="stylesheet">
<style>
:root{
  --canvas:#8c8c8c;
  --navy:#19478d;
  --blue:#0356a4;
  --white:#ffffff;
  --ink:#3c3c3c;
  --muted:#7a7a7a;
  --panel:rgba(25,71,141,.92);
}
*{box-sizing:border-box;margin:0;padding:0}
html,body{width:1200px;height:1075px;overflow:hidden;background:var(--canvas)}
body{position:relative;font-family:'Montserrat',Arial,sans-serif;color:var(--ink)}
.slide{position:absolute;width:244px;height:137px;background:var(--white);overflow:hidden}
.a{position:absolute}
.photo{position:absolute}
.ph-office{background:linear-gradient(135deg,#b9c3cf,#6d7d92 55%,#3c4a60)}
.ph-blue{background:linear-gradient(160deg,#5b7fbf,#2a5196 55%,#163c7a)}
.ph-city{background:linear-gradient(180deg,#9fb5cf,#6a88ab 50%,#3f5c7a)}
.ph-green{background:linear-gradient(160deg,#c9d6e2,#7f9bb4 45%,#5c7b4e)}
.ph-warm{background:linear-gradient(150deg,#d9cfc5,#a69484 55%,#5e5048)}
.ph-dusk{background:linear-gradient(180deg,#6f7f97,#4a566a 55%,#c08a4a)}
.heading{font-weight:600;color:var(--blue);font-size:6.4px;letter-spacing:.1px;text-transform:uppercase}
.title{font-weight:600;font-size:7.6px;line-height:1.25}
.copy{font-size:2.6px;line-height:1.35;color:var(--ink)}
.copy.light{color:#e6ecf6}
.label{font-size:3.2px;font-weight:600;color:var(--blue)}
.quote{font-weight:600;font-size:6px;line-height:1.3;color:var(--blue)}
.quote.light{color:var(--white);font-size:4.6px}
.pill{background:var(--blue);color:var(--white);font-size:2.8px;font-weight:600;padding:1px 2px}
.icon{position:absolute;width:11px;height:11px;color:var(--blue)}
.icon.white{color:var(--white)}
.round{border-radius:50%}
.white-text{color:var(--white)}
.blue-fill{background:var(--navy)}
.rule{position:absolute;height:.6px;background:var(--blue)}
</style>
</head>
<body>
<svg width="0" height="0" style="position:absolute">
  <defs>
    <symbol id="i-chart" viewBox="0 0 20 20"><rect x="2" y="3" width="16" height="12" fill="none" stroke="currentColor" stroke-width="1.3"/><path d="M5 13V9M9 13V6M13 13V10M16 13V7" stroke="currentColor" stroke-width="1.5"/><path d="M7 18h6" stroke="currentColor" stroke-width="1.3"/></symbol>
    <symbol id="i-people" viewBox="0 0 20 20"><circle cx="6" cy="6" r="2.5" fill="currentColor"/><circle cx="14" cy="6" r="2.5" fill="currentColor"/><circle cx="10" cy="9" r="2.8" fill="currentColor"/><path d="M3 17c0-4 3-6 7-6s7 2 7 6z" fill="currentColor"/></symbol>
    <symbol id="i-doc" viewBox="0 0 20 20"><rect x="4" y="2" width="12" height="16" fill="none" stroke="currentColor" stroke-width="1.3"/><path d="M7 6h6M7 9h6M7 12h6M7 15h4" stroke="currentColor" stroke-width="1.2"/></symbol>
    <symbol id="i-lock" viewBox="0 0 20 20"><rect x="4" y="9" width="12" height="9" rx="1" fill="currentColor"/><path d="M7 9V6a3 3 0 0 1 6 0v3" fill="none" stroke="currentColor" stroke-width="1.6"/></symbol>
    <symbol id="i-play" viewBox="0 0 20 20"><rect x="2" y="3" width="16" height="12" fill="none" stroke="currentColor" stroke-width="1.4"/><path d="M8 6l5 3-5 3z" fill="currentColor"/><path d="M6 18h8" stroke="currentColor" stroke-width="1.4"/></symbol>
    <symbol id="i-calendar" viewBox="0 0 20 20"><rect x="3" y="4" width="14" height="13" rx="1" fill="currentColor"/><rect x="5" y="8" width="10" height="7" fill="#fff" opacity=".35"/><path d="M7 2v4M13 2v4" stroke="currentColor" stroke-width="1.6"/></symbol>
    <symbol id="i-org" viewBox="0 0 20 20"><circle cx="10" cy="4" r="2.4" fill="none" stroke="currentColor" stroke-width="1.2"/><circle cx="4" cy="15" r="2.4" fill="none" stroke="currentColor" stroke-width="1.2"/><circle cx="10" cy="15" r="2.4" fill="none" stroke="currentColor" stroke-width="1.2"/><circle cx="16" cy="15" r="2.4" fill="none" stroke="currentColor" stroke-width="1.2"/><path d="M10 6.5v6M4 12.5V10h12v2.5" fill="none" stroke="currentColor" stroke-width="1.2"/></symbol>
    <symbol id="i-download" viewBox="0 0 20 20"><path d="M10 2v9M6 7l4 4 4-4" fill="none" stroke="currentColor" stroke-width="1.8"/><path d="M3 12v5h14v-5" fill="none" stroke="currentColor" stroke-width="1.8"/></symbol>
    <symbol id="i-quote" viewBox="0 0 20 20"><path d="M2 16V9c0-4 2-6 6-6v3c-2 0-3 1-3 3h3v7zM11 16V9c0-4 2-6 6-6v3c-2 0-3 1-3 3h3v7z" fill="currentColor"/></symbol>
    <symbol id="i-building" viewBox="0 0 20 20"><rect x="4" y="3" width="12" height="15" fill="currentColor"/><path d="M7 6h2M11 6h2M7 9h2M11 9h2M7 12h2M11 12h2" stroke="#fff" stroke-width="1.2"/></symbol>
  </defs>
</svg>

<!-- Row 1 -->
<section class="slide" style="left:54px;top:48px">
  <div class="photo ph-blue" style="left:0;top:0;width:244px;height:112px" role="img" aria-label="Modern waterfront architecture photo tinted blue"></div>
  <div class="a title white-text" style="left:0;top:45px;width:244px;text-align:center;font-size:8.2px">Lorem ipsum dolor sit amet, consectetur</div>
  <div class="a white-text" style="left:0;top:61px;width:244px;text-align:center;font-size:4px;font-weight:600">Lorem ipsum dolor sit amet, consectetur</div>
  <div class="a" style="left:24px;top:118px;font-size:3.4px;font-weight:600;color:var(--navy)">HARBOURLINE CAPITAL</div>
  <div class="a" style="left:186px;top:121px;font-size:3.2px;font-weight:600;color:var(--navy)">www.harbourline.com</div>
</section>

<section class="slide" style="left:331px;top:48px">
  <div class="photo ph-warm" style="left:0;top:0;width:122px;height:137px" role="img" aria-label="Two colleagues reviewing documents together"></div>
  <div class="a blue-fill" style="left:122px;top:0;width:122px;height:137px"></div>
  <div class="a title white-text" style="left:143px;top:33px">Introduction</div>
  <p class="a copy light" style="left:143px;top:50px;width:88px">Lorem ipsum dolor sit amet, consectetur adipiscing elit, sed do eiusmod tempor incididunt ut labore et dolore magna aliqua. Ut enim ad minim veniam, quis nostrud exercitation ullamco laboris nisi ut aliquip ex ea commodo consequat. Duis aute irure dolor in reprehenderit in voluptate velit esse cillum dolore eu fugiat nulla pariatur. Excepteur sint occaecat cupidatat non proident, sunt in culpa qui officia deserunt mollit anim id est laborum. Lorem ipsum dolor sit amet, consectetur adipiscing elit, sed do eiusmod tempor incididunt ut labore et dolore magna aliqua. Ut enim ad minim veniam, quis nostrud exercitation ullamco laboris nisi ut aliquip ex ea commodo consequat.</p>
</section>

<section class="slide" style="left:607px;top:48px">
  <div class="photo ph-green" style="left:0;top:0;width:244px;height:137px" role="img" aria-label="Glass office building with trees"></div>
  <div class="a" style="left:20px;top:0;width:95px;height:114px;background:var(--white)"></div>
  <div class="a title" style="left:34px;top:19px;color:var(--blue)">About Us</div>
  <p class="a copy" style="left:32px;top:33px;width:76px">Lorem ipsum dolor sit amet, consectetur adipiscing elit, sed do eiusmod tempor incididunt ut labore et dolore magna aliqua. Ut enim ad minim veniam, quis nostrud exercitation ullamco laboris nisi ut aliquip ex ea commodo consequat. Duis aute irure dolor in reprehenderit in voluptate velit esse cillum dolore eu fugiat nulla pariatur. Excepteur sint occaecat cupidatat non proident, sunt in culpa qui officia deserunt mollit anim id est laborum. Lorem ipsum dolor sit amet, consectetur adipiscing elit, sed do eiusmod tempor incididunt ut labore et dolore magna aliqua.</p>
</section>

<section class="slide" style="left:885px;top:48px">
  <div class="photo ph-blue" style="left:0;top:0;width:244px;height:137px" role="img" aria-label="Financial market data screens tinted blue"></div>
  <div class="a white-text" style="left:17px;top:29px;font-size:4.6px;font-weight:600">Lorem Ipsum</div>
  <p class="a copy light" style="left:12px;top:36px;width:52px">Lorem ipsum dolor sit amet, consectetur adipiscing elit, sed do eiusmod tempor incididunt ut labore et dolore magna aliqua. Ut enim ad minim veniam, quis nostrud exercitation ullamco laboris nisi ut aliquip ex ea commodo consequat. Duis aute irure dolor in reprehenderit in voluptate velit esse cillum dolore eu fugiat nulla pariatur. Excepteur sint occaecat cupidatat non proident, sunt in culpa qui officia deserunt mollit anim id est laborum magna aliqua.</p>
  <div class="a" style="left:95px;top:23px;width:130px;height:96px;background:var(--white)"></div>
  <svg class="icon" style="left:108px;top:34px;width:8px;height:8px"><use href="#i-play"/></svg>
  <svg class="icon" style="left:178px;top:34px;width:8px;height:8px"><use href="#i-chart"/></svg>
  <svg class="icon" style="left:108px;top:76px;width:8px;height:8px"><use href="#i-lock"/></svg>
  <svg class="icon" style="left:178px;top:76px;width:8px;height:8px"><use href="#i-lock"/></svg>
  <div class="a label" style="left:108px;top:46px">Lorem Ipsum</div>
  <p class="a copy" style="left:108px;top:51px;width:50px">Lorem ipsum dolor sit amet, consectetur adipiscing elit, sed</p>
  <div class="a label" style="left:178px;top:46px">Lorem Ipsum</div>
  <p class="a copy" style="left:178px;top:51px;width:42px">Lorem ipsum dolor sit amet, consectetur adipiscing elit, sed</p>
  <div class="a label" style="left:108px;top:88px">Lorem Ipsum</div>
  <p class="a copy" style="left:108px;top:93px;width:50px">Lorem ipsum dolor sit amet, consectetur adipiscing elit, sed</p>
  <div class="a label" style="left:178px;top:88px">Lorem Ipsum</div>
  <p class="a copy" style="left:178px;top:93px;width:42px">Lorem ipsum dolor sit amet, consectetur adipiscing elit, sed</p>
</section>

<!-- Row 2 -->
<section class="slide" style="left:54px;top:218px">
  <div class="a heading" style="left:14px;top:14px">Meet Our Team</div>
  <div class="photo ph-office" style="left:14px;top:28px;width:35px;height:72px" role="img" aria-label="Portrait of team member"></div>
  <div class="photo ph-office" style="left:50px;top:28px;width:35px;height:72px" role="img" aria-label="Portrait of team member"></div>
  <div class="photo ph-office" style="left:86px;top:28px;width:35px;height:72px" role="img" aria-label="Portrait of team member"></div>
  <div class="photo ph-office" style="left:122px;top:28px;width:35px;height:72px" role="img" aria-label="Portrait of team member"></div>
  <div class="photo ph-office" style="left:158px;top:28px;width:35px;height:72px" role="img" aria-label="Portrait of team member"></div>
  <div class="photo ph-office" style="left:194px;top:28px;width:35px;height:72px" role="img" aria-label="Portrait of team member"></div>
  <div class="a" style="left:14px;top:100px;width:215px;height:12px;background:#e6e6e6"></div>
  <div class="a" style="left:14px;top:102px;width:215px;display:grid;grid-template-columns:repeat(6,1fr);text-align:center;font-size:2.8px;line-height:1.5">
    <div><b style="color:var(--blue)">Owen Hale</b><br>CEO/President</div>
    <div><b style="color:var(--blue)">Nora Vale</b><br>VP-Finance</div>
    <div><b style="color:var(--blue)">Iris Cole</b><br>Human Resource</div>
    <div><b style="color:var(--blue)">Mara Dunn</b><br>Managing Director</div>
    <div><b style="color:var(--blue)">Leo Grant</b><br>Manager-Delivery</div>
    <div><b style="color:var(--blue)">Evan Shaw</b><br>Manager-Accounts</div>
  </div>
</section>

<section class="slide" style="left:331px;top:218px">
  <div class="a heading" style="left:14px;top:14px">Our Services</div>
  <svg class="icon" style="left:14px;top:33px"><use href="#i-chart"/></svg>
  <svg class="icon" style="left:86px;top:33px"><use href="#i-doc"/></svg>
  <svg class="icon" style="left:14px;top:66px"><use href="#i-people"/></svg>
  <svg class="icon" style="left:86px;top:66px"><use href="#i-chart"/></svg>
  <svg class="icon" style="left:14px;top:102px"><use href="#i-doc"/></svg>
  <svg class="icon" style="left:86px;top:102px"><use href="#i-org"/></svg>
  <div class="a label" style="left:36px;top:34px;font-size:2.8px">Lorem ipsum dolor</div><p class="a copy" style="left:36px;top:39px;width:40px">Lorem ipsum dolor sit amet, consectetur adipiscing elit.</p>
  <div class="a label" style="left:110px;top:34px;font-size:2.8px">Lorem ipsum dolor</div><p class="a copy" style="left:110px;top:39px;width:40px">Lorem ipsum dolor sit amet, consectetur adipiscing elit.</p>
  <div class="a label" style="left:36px;top:67px;font-size:2.8px">Lorem ipsum dolor</div><p class="a copy" style="left:36px;top:72px;width:40px">Lorem ipsum dolor sit amet, consectetur adipiscing elit.</p>
  <div class="a label" style="left:110px;top:67px;font-size:2.8px">Lorem ipsum dolor</div><p class="a copy" style="left:110px;top:72px;width:40px">Lorem ipsum dolor sit amet, consectetur adipiscing elit.</p>
  <div class="a label" style="left:36px;top:103px;font-size:2.8px">Lorem ipsum dolor</div><p class="a copy" style="left:36px;top:108px;width:40px">Lorem ipsum dolor sit amet, consectetur adipiscing elit.</p>
  <div class="a label" style="left:110px;top:103px;font-size:2.8px">Lorem ipsum dolor</div><p class="a copy" style="left:110px;top:108px;width:40px">Lorem ipsum dolor sit amet, consectetur adipiscing elit.</p>
  <div class="photo ph-warm" style="left:162px;top:12px;width:73px;height:114px" role="img" aria-label="Woman working on a laptop"></div>
</section>

<section class="slide" style="left:607px;top:218px">
  <div class="a blue-fill" style="left:0;top:0;width:100px;height:137px"></div>
  <svg class="icon white" style="left:42px;top:22px;width:18px;height:18px"><use href="#i-quote"/></svg>
  <p class="a quote light" style="left:18px;top:49px;width:66px;text-align:center;font-size:4.8px">“Lorem ipsum dolor sit amet, consectetur adipiscing elit. Phasellus sodales, ligula ultrices tempus ristique, tellus justo aliquam dui, nec Lorem ipsum dolor sit amet, consectetur</p>
  <div class="a heading" style="left:114px;top:11px;font-size:5.6px">Testimonials</div>
  <div class="photo ph-office round" style="left:114px;top:31px;width:21px;height:21px" role="img" aria-label="Client portrait"></div>
  <div class="photo ph-warm round" style="left:114px;top:66px;width:21px;height:21px" role="img" aria-label="Client portrait"></div>
  <div class="photo ph-warm round" style="left:114px;top:101px;width:21px;height:21px" role="img" aria-label="Client portrait"></div>
  <div class="a label" style="left:143px;top:33px">Lorem Ipsum</div><p class="a copy" style="left:143px;top:38px;width:90px">Lorem ipsum dolor sit amet, consectetur adipiscing elit, sed do eiusmod tempor incididunt ut labore et dolore magna aliqua. Ut enim ad minim veniam, quis nostrud</p>
  <div class="a label" style="left:143px;top:68px">Lorem Ipsum</div><p class="a copy" style="left:143px;top:73px;width:90px">Lorem ipsum dolor sit amet, consectetur adipiscing elit, sed do eiusmod tempor incididunt ut labore et dolore magna aliqua. Ut enim ad minim veniam, quis nostrud</p>
  <div class="a label" style="left:143px;top:103px">Lorem Ipsum</div><p class="a copy" style="left:143px;top:108px;width:90px">Lorem ipsum dolor sit amet, consectetur adipiscing elit, sed do eiusmod tempor incididunt ut labore et dolore magna aliqua. Ut enim ad minim veniam, quis nostrud</p>
</section>

<section class="slide" style="left:885px;top:218px">
  <div class="photo ph-office" style="left:0;top:0;width:111px;height:137px" role="img" aria-label="Trading desk with monitors"></div>
  <div class="a heading" style="left:152px;top:12px;font-size:5.6px">Our Portfolio</div>
  <svg class="icon" style="left:126px;top:32px;width:15px;height:15px"><use href="#i-chart"/></svg>
  <svg class="icon" style="left:126px;top:67px;width:15px;height:15px"><use href="#i-calendar"/></svg>
  <svg class="icon" style="left:126px;top:102px;width:15px;height:15px"><use href="#i-doc"/></svg>
  <div class="a label" style="left:155px;top:33px">Lorem Ipsum</div><p class="a copy" style="left:155px;top:38px;width:80px">Lorem ipsum dolor sit amet, consectetur adipiscing elit, sed do eiusmod tempor incididunt ut labore et dolore magna aliqua. Ut enim ad minim veniam</p>
  <div class="a label" style="left:155px;top:68px">Lorem Ipsum</div><p class="a copy" style="left:155px;top:73px;width:80px">Lorem ipsum dolor sit amet, consectetur adipiscing elit, sed do eiusmod tempor incididunt ut labore et dolore magna aliqua. Ut enim ad minim veniam</p>
  <div class="a label" style="left:155px;top:104px">Lorem Ipsum</div><p class="a copy" style="left:155px;top:109px;width:80px">Lorem ipsum dolor sit amet, consectetur adipiscing elit, sed do eiusmod tempor incididunt ut labore et dolore magna aliqua. Ut enim ad minim veniam</p>
</section>

<!-- Row 3 -->
<section class="slide" style="left:54px;top:379px">
  <div class="photo ph-blue" style="left:0;top:0;width:244px;height:64px" role="img" aria-label="Boardroom interior tinted blue"></div>
  <p class="a white-text" style="left:20px;top:26px;width:204px;text-align:center;font-size:5px;font-weight:600;line-height:1.3">“Lorem ipsum dolor sit amet, consectetur adipiscing elit. Phasellus sodales, ligula ultrices tempus ristique, tellus justo aliquam dui,</p>
  <svg class="icon" style="left:44px;top:74px;width:22px;height:22px"><use href="#i-chart"/></svg>
  <svg class="icon" style="left:112px;top:74px;width:22px;height:22px"><use href="#i-doc"/></svg>
  <svg class="icon" style="left:180px;top:74px;width:22px;height:22px"><use href="#i-doc"/></svg>
  <div class="a label" style="left:30px;top:101px;width:50px;text-align:center">Lorem Ipsum</div><p class="a copy" style="left:28px;top:107px;width:54px;text-align:center">Lorem ipsum dolor sit amet, consectetur adipiscing elit, sed do eiusmod tempor incididunt ut labore</p>
  <div class="a label" style="left:98px;top:101px;width:50px;text-align:center">Lorem Ipsum</div><p class="a copy" style="left:96px;top:107px;width:54px;text-align:center">Lorem ipsum dolor sit amet, consectetur adipiscing elit, sed do eiusmod tempor incididunt ut labore</p>
  <div class="a label" style="left:166px;top:101px;width:50px;text-align:center">Lorem Ipsum</div><p class="a copy" style="left:164px;top:107px;width:54px;text-align:center">Lorem ipsum dolor sit amet, consectetur adipiscing elit, sed do eiusmod tempor incididunt ut labore</p>
</section>

<section class="slide" style="left:331px;top:379px">
  <div class="photo ph-office" style="left:0;top:0;width:45px;height:70px" role="img" aria-label="Meeting room"></div>
  <div class="photo ph-warm" style="left:47px;top:0;width:48px;height:55px" role="img" aria-label="Team at a table"></div>
  <div class="photo ph-office" style="left:97px;top:0;width:48px;height:58px" role="img" aria-label="Laptop on a desk"></div>
  <div class="photo ph-warm" style="left:0;top:72px;width:45px;height:65px" role="img" aria-label="Business people talking"></div>
  <div class="photo ph-office" style="left:47px;top:57px;width:48px;height:38px" role="img" aria-label="Office workspace"></div>
  <div class="photo ph-warm" style="left:47px;top:97px;width:48px;height:40px" role="img" aria-label="Person working on laptop"></div>
  <div class="photo ph-warm" style="left:97px;top:60px;width:48px;height:77px" role="img" aria-label="Celebrating colleague"></div>
  <div class="a title" style="left:167px;top:22px;color:var(--blue);font-size:7px;font-weight:500">Lorem Ipsum</div>
  <p class="a copy" style="left:159px;top:35px;width:78px;text-align:center">Lorem ipsum dolor sit amet, consectetur adipiscing elit, sed do eiusmod tempor incididunt ut labore et dolore magna aliqua. Ut enim ad minim veniam, quis nostrud exercitation ullamco laboris nisi ut aliquip ex ea commodo consequat. Duis aute irure dolor in reprehenderit in voluptate velit esse cillum dolore eu fugiat nulla pariatur. Excepteur sint occaecat cupidatat non proident, sunt in culpa qui officia deserunt mollit anim id est laborum. Lorem ipsum dolor sit amet, consectetur adipiscing elit, sed do eiusmod tempor incididunt ut labore et dolore magna aliqua. Ut enim ad minim veniam, quis nostrud exercitation ullamco.</p>
</section>

<section class="slide" style="left:607px;top:379px">
  <div class="a heading" style="left:0;top:13px;width:244px;text-align:center;font-weight:500">Our Team</div>
  <div class="photo ph-office round" style="left:22px;top:34px;width:36px;height:36px" role="img" aria-label="Team member portrait"></div>
  <div class="photo ph-office round" style="left:134px;top:34px;width:36px;height:36px" role="img" aria-label="Team member portrait"></div>
  <div class="photo ph-warm round" style="left:22px;top:83px;width:36px;height:36px" role="img" aria-label="Team member portrait"></div>
  <div class="photo ph-warm round" style="left:134px;top:83px;width:36px;height:36px" role="img" aria-label="Team member portrait"></div>
  <span class="a pill" style="left:62px;top:37px">Lorem Ipsum</span><p class="a copy" style="left:62px;top:44px;width:52px">Lorem ipsum dolor sit amet, consectetur adipiscing elit, sed do eiusmod tempor incididunt ut labore et dolore magna aliqua. Ut enim ad minim</p>
  <span class="a pill" style="left:174px;top:37px">Lorem Ipsum</span><p class="a copy" style="left:174px;top:44px;width:52px">Lorem ipsum dolor sit amet, consectetur adipiscing elit, sed do eiusmod tempor incididunt ut labore et dolore magna aliqua. Ut enim ad minim</p>
  <span class="a pill" style="left:62px;top:85px">Lorem Ipsum</span><p class="a copy" style="left:62px;top:92px;width:52px">Lorem ipsum dolor sit amet, consectetur adipiscing elit, sed do eiusmod tempor incididunt ut labore et dolore magna aliqua. Ut enim ad minim</p>
  <span class="a pill" style="left:174px;top:85px">Lorem Ipsum</span><p class="a copy" style="left:174px;top:92px;width:52px">Lorem ipsum dolor sit amet, consectetur adipiscing elit, sed do eiusmod tempor incididunt ut labore et dolore magna aliqua. Ut enim ad minim</p>
</section>

<section class="slide" style="left:885px;top:379px">
  <p class="a quote" style="left:5px;top:40px;width:56px;text-align:center;font-size:5.4px;font-weight:500">“Lorem ipsum dolor sit amet, consectetur adipiscing elit.</p>
  <div class="photo ph-warm" style="left:61px;top:0;width:93px;height:137px" role="img" aria-label="Smiling woman with a laptop"></div>
  <svg class="icon" style="left:165px;top:18px;width:10px;height:10px"><use href="#i-lock"/></svg>
  <svg class="icon" style="left:165px;top:58px;width:10px;height:10px"><use href="#i-people"/></svg>
  <svg class="icon" style="left:165px;top:98px;width:10px;height:10px"><use href="#i-building"/></svg>
  <div class="a label" style="left:184px;top:17px;font-size:2.9px">Lorem Ipsum Dolor</div><p class="a copy" style="left:184px;top:22px;width:50px">Lorem ipsum dolor sit amet, consectetur adipiscing elit, sed do eiusmod tempor incididunt ut labore et dolore magna aliqua. Ut enim ad minim</p>
  <div class="a label" style="left:184px;top:57px;font-size:2.9px">Lorem Ipsum Dolor</div><p class="a copy" style="left:184px;top:62px;width:50px">Lorem ipsum dolor sit amet, consectetur adipiscing elit, sed do eiusmod tempor incididunt ut labore et dolore magna aliqua. Ut enim ad minim</p>
  <div class="a label" style="left:184px;top:97px;font-size:2.9px">Lorem Ipsum Dolor</div><p class="a copy" style="left:184px;top:102px;width:50px">Lorem ipsum dolor sit amet, consectetur adipiscing elit, sed do eiusmod tempor incididunt ut labore et dolore magna aliqua. Ut enim ad minim</p>
</section>

<!-- Row 4 -->
<section class="slide" style="left:54px;top:546px">
  <p class="a quote" style="left:4px;top:40px;width:52px;text-align:center;font-size:5.8px;font-weight:500">“Lorem ipsum dolor sit amet, consectetur adipiscing</p>
  <div class="a blue-fill" style="left:56px;top:0;width:80px;height:137px"></div>
  <div class="photo ph-office" style="left:134px;top:0;width:110px;height:137px" role="img" aria-label="Hands using a tablet"></div>
  <div class="a white-text" style="left:70px;top:16px;font-size:3.2px;font-weight:600">Lorem Ipsum Dolor</div><p class="a copy light" style="left:70px;top:22px;width:56px">Lorem ipsum dolor sit amet, consectetur adipiscing elit, sed do eiusmod tempor incididunt ut labore et dolore magna aliqua. Ut enim ad minim</p>
  <div class="a white-text" style="left:70px;top:57px;font-size:3.2px;font-weight:600">Lorem Ipsum Dolor</div><p class="a copy light" style="left:70px;top:63px;width:56px">Lorem ipsum dolor sit amet, consectetur adipiscing elit, sed do eiusmod tempor incididunt ut labore et dolore magna aliqua. Ut enim ad minim</p>
  <div class="a white-text" style="left:70px;top:97px;font-size:3.2px;font-weight:600">Lorem Ipsum Dolor</div><p class="a copy light" style="left:70px;top:103px;width:56px">Lorem ipsum dolor sit amet, consectetur adipiscing elit, sed do eiusmod tempor incididunt ut labore et dolore magna aliqua. Ut enim ad minim</p>
</section>

<section class="slide" style="left:331px;top:538px">
  <div class="a blue-fill" style="left:0;top:0;width:128px;height:137px"></div>
  <div class="a white-text" style="left:16px;top:20px;font-size:6.4px;font-weight:600;line-height:1.35">Lorem ipsum dolor<br>sit amet, consectetur</div>
  <p class="a copy light" style="left:16px;top:46px;width:100px">“Lorem ipsum dolor sit amet, consectetur adipiscing elit. Phasellus sodales, ligula ultrices tempus ristique, tellus justo aliquam dui, nec Lorem ipsum dolor sit amet, consectetur “Lorem ipsum dolor sit amet, consectetur adipiscing elit. Phasellus sodales, ligula ultrices tempus ristique, tellus justo aliquam dui, nec Lorem ipsum dolor sit amet, consectetur “Lorem ipsum dolor sit amet, consectetur adipiscing elit. Phasellus sodales, ligula ultrices tempus ristique, tellus justo aliquam dui, nec Lorem ipsum dolor sit amet, consectetur “Lorem ipsum dolor sit amet, consectetur adipiscing elit. Phasellus sodales, ligula ultrices tempus ristique, tellus justo aliquam dui, nec Lorem ipsum dolor sit amet, consectetur.</p>
  <svg class="icon" style="left:143px;top:18px;width:14px;height:14px"><use href="#i-people"/></svg>
  <svg class="icon" style="left:143px;top:58px;width:14px;height:14px"><use href="#i-building"/></svg>
  <svg class="icon" style="left:143px;top:97px;width:14px;height:14px"><use href="#i-play"/></svg>
  <div class="a label" style="left:166px;top:17px">Lorem Ipsum</div><p class="a copy" style="left:166px;top:22px;width:64px">Lorem ipsum dolor sit amet, consectetur adipiscing elit, sed do eiusmod tempor incididunt ut labore et dolore magna aliqua. Ut enim ad minim</p>
  <div class="a label" style="left:166px;top:57px">Lorem Ipsum</div><p class="a copy" style="left:166px;top:62px;width:64px">Lorem ipsum dolor sit amet, consectetur adipiscing elit, sed do eiusmod tempor incididunt ut labore et dolore magna aliqua. Ut enim ad minim</p>
  <div class="a label" style="left:166px;top:96px">Lorem Ipsum</div><p class="a copy" style="left:166px;top:101px;width:64px">Lorem ipsum dolor sit amet, consectetur adipiscing elit, sed do eiusmod tempor incididunt ut labore et dolore magna aliqua. Ut enim ad minim</p>
</section>

<section class="slide" style="left:607px;top:538px">
  <div class="photo ph-office" style="left:16px;top:5px;width:216px;height:70px" role="img" aria-label="Team meeting in a bright office"></div>
  <div class="rule" style="left:14px;top:87px;width:66px"></div>
  <p class="a quote" style="left:14px;top:95px;width:68px;text-align:center;font-size:5.4px;font-weight:500">“Lorem ipsum dolor sit amet, consectetur</p>
  <div class="rule" style="left:14px;top:118px;width:66px"></div>
  <p class="a copy" style="left:88px;top:83px;width:146px">“Lorem ipsum dolor sit amet, consectetur adipiscing elit. Phasellus sodales, ligula ultrices tempus ristique, tellus justo aliquam dui, nec Lorem ipsum dolor sit amet, consectetur “Lorem ipsum dolor sit amet, consectetur adipiscing elit. Phasellus sodales, ligula ultrices tempus ristique, tellus justo aliquam dui, nec Lorem ipsum dolor sit amet, consectetur “Lorem ipsum dolor sit amet, consectetur adipiscing elit. Phasellus sodales, ligula ultrices tempus ristique, tellus justo aliquam dui, nec Lorem ipsum dolor sit amet, consectetur “Lorem ipsum dolor sit amet, consectetur adipiscing elit. Phasellus sodales, ligula ultrices tempus ristique, tellus justo aliquam dui, nec Lorem ipsum dolor sit amet.</p>
</section>

<section class="slide" style="left:885px;top:538px">
  <div class="photo ph-blue" style="left:0;top:0;width:244px;height:137px" role="img" aria-label="Office workspace tinted deep blue"></div>
  <div class="a white-text" style="left:0;top:61px;width:244px;text-align:center;font-size:12.4px;font-weight:700;letter-spacing:.2px">SECTION TITLE HERE</div>
</section>

<!-- Row 5 -->
<section class="slide" style="left:54px;top:714px">
  <span class="a pill" style="left:42px;top:26px">Lorem Ipsum</span><p class="a copy" style="left:20px;top:36px;width:58px;text-align:right">Lorem ipsum dolor sit amet, consectetur adipiscing elit, sed do eiusmod tempor incididunt ut labore et dolore magna aliqua. Ut enim ad minim veniam, quis</p>
  <span class="a pill" style="left:42px;top:81px">Lorem Ipsum</span><p class="a copy" style="left:20px;top:91px;width:58px;text-align:right">Lorem ipsum dolor sit amet, consectetur adipiscing elit, sed do eiusmod tempor incididunt ut labore et dolore magna aliqua. Ut enim ad minim veniam, quis</p>
  <div class="photo ph-blue" style="left:84px;top:0;width:76px;height:137px" role="img" aria-label="Blue-tinted office photo"></div>
  <p class="a quote light" style="left:90px;top:26px;width:64px;text-align:center;font-size:5.2px;font-weight:500">“Lorem ipsum dolor sit amet, consectetur adipiscing elit. Phasellus sodales, ligula ultrices tempus ristique, tellus justo aliquam dui,</p>
  <span class="a pill" style="left:174px;top:26px">Lorem Ipsum</span><p class="a copy" style="left:174px;top:36px;width:58px">Lorem ipsum dolor sit amet, consectetur adipiscing elit, sed do eiusmod tempor incididunt ut labore et dolore magna aliqua. Ut enim ad minim veniam, quis</p>
  <span class="a pill" style="left:174px;top:81px">Lorem Ipsum</span><p class="a copy" style="left:174px;top:91px;width:58px">Lorem ipsum dolor sit amet, consectetur adipiscing elit, sed do eiusmod tempor incididunt ut labore et dolore magna aliqua. Ut enim ad minim veniam, quis</p>
</section>

<section class="slide" style="left:331px;top:714px">
  <div class="a heading" style="left:0;top:13px;width:244px;text-align:center;font-weight:500">Our Team</div>
  <div class="photo ph-office" style="left:0;top:28px;width:244px;height:58px" role="img" aria-label="Overhead view of a collaborative desk"></div>
  <div class="a blue-fill" style="left:20px;top:55px;width:59px;height:47px"></div>
  <div class="a blue-fill" style="left:89px;top:55px;width:59px;height:47px"></div>
  <div class="a blue-fill" style="left:158px;top:55px;width:59px;height:47px"></div>
  <svg class="icon white" style="left:42px;top:65px;width:15px;height:15px"><use href="#i-chart"/></svg>
  <svg class="icon white" style="left:111px;top:65px;width:15px;height:15px"><use href="#i-building"/></svg>
  <svg class="icon white" style="left:180px;top:65px;width:15px;height:15px"><use href="#i-people"/></svg>
  <div class="a white-text" style="left:20px;top:91px;width:59px;text-align:center;font-size:3.2px;font-weight:600">Lorem Ipsum Dolor</div>
  <div class="a white-text" style="left:89px;top:91px;width:59px;text-align:center;font-size:3.2px;font-weight:600">Lorem Ipsum Dolor</div>
  <div class="a white-text" style="left:158px;top:91px;width:59px;text-align:center;font-size:3.2px;font-weight:600">Lorem Ipsum Dolor</div>
  <p class="a copy" style="left:20px;top:108px;width:59px;text-align:center">Lorem ipsum dolor sit amet, consectetur adipiscing elit, sed do eiusmod tempor incididunt ut</p>
  <p class="a copy" style="left:89px;top:108px;width:59px;text-align:center">Lorem ipsum dolor sit amet, consectetur adipiscing elit, sed do eiusmod tempor incididunt ut</p>
  <p class="a copy" style="left:158px;top:108px;width:59px;text-align:center">Lorem ipsum dolor sit amet, consectetur adipiscing elit, sed do eiusmod tempor incididunt ut</p>
</section>

<section class="slide" style="left:607px;top:714px">
  <div class="photo ph-blue" style="left:0;top:0;width:128px;height:137px" role="img" aria-label="City street tinted blue"></div>
  <div class="a white-text" style="left:15px;top:31px;font-size:6.6px;font-weight:600">Lorem ipsum dolor sit</div>
  <p class="a copy light" style="left:15px;top:45px;width:100px">“Lorem ipsum dolor sit amet, consectetur adipiscing elit. Phasellus sodales, ligula ultrices tempus ristique, tellus justo aliquam dui, nec Lorem ipsum dolor sit amet, consectetur “Lorem ipsum dolor sit amet, consectetur adipiscing elit. Phasellus sodales, ligula ultrices tempus ristique, tellus justo aliquam dui, nec Lorem ipsum dolor sit amet, consectetur “Lorem ipsum dolor sit amet, consectetur adipiscing elit. Phasellus sodales, ligula ultrices tempus ristique, tellus justo aliquam dui, nec Lorem ipsum dolor sit amet, consectetur adipiscing elit.</p>
  <div class="photo ph-office" style="left:128px;top:0;width:116px;height:137px" role="img" aria-label="Desk with laptops and documents from above"></div>
</section>

<section class="slide" style="left:885px;top:714px">
  <div class="a blue-fill" style="left:0;top:0;width:244px;height:52px"></div>
  <div class="a white-text" style="left:14px;top:12px;font-size:6.6px;font-weight:600">EDIT TITLE HERE</div>
  <p class="a copy light" style="left:14px;top:25px;width:128px">“Lorem ipsum dolor sit amet, consectetur adipiscing elit. Phasellus sodales, ligula ultrices tempus ristique, tellus justo aliquam dui, nec Lorem ipsum dolor sit amet, consectetur “Lorem ipsum dolor sit amet,</p>
  <div class="a" style="left:14px;top:63px;font-size:3.8px;font-weight:600;color:var(--ink)">Lorem ipsum dolor sit amet</div>
  <p class="a copy" style="left:14px;top:71px;width:128px">“Lorem ipsum dolor sit amet, consectetur adipiscing elit. Phasellus sodales, ligula ultrices tempus ristique, tellus justo aliquam dui, nec Lorem ipsum dolor sit amet, consectetur “Lorem ipsum dolor sit amet, consectetur adipiscing elit. Phasellus sodales, ligula ultrices tempus ristique, tellus justo aliquam dui, nec Lorem ipsum dolor sit amet, consectetur “Lorem ipsum dolor sit amet, consectetur adipiscing elit. Phasellus sodales, ligula ultrices tempus ristique, tellus justo aliquam dui.</p>
  <div class="photo ph-city" style="left:146px;top:20px;width:87px;height:106px" role="img" aria-label="City skyline across the water"></div>
</section>

<!-- Row 6 -->
<section class="slide" style="left:54px;top:882px">
  <div class="a heading" style="left:14px;top:13px;font-size:6px">Edit Title Here</div>
  <div class="photo ph-blue" style="left:18px;top:29px;width:66px;height:92px" role="img" aria-label="Blue-tinted business photo"></div>
  <div class="photo ph-blue" style="left:89px;top:29px;width:66px;height:92px" role="img" aria-label="Blue-tinted business photo"></div>
  <div class="photo ph-blue" style="left:160px;top:29px;width:66px;height:92px" role="img" aria-label="Blue-tinted business photo"></div>
  <svg class="icon white" style="left:42px;top:44px;width:18px;height:18px"><use href="#i-calendar"/></svg>
  <svg class="icon white" style="left:113px;top:44px;width:18px;height:18px"><use href="#i-chart"/></svg>
  <svg class="icon white" style="left:184px;top:44px;width:18px;height:18px"><use href="#i-download"/></svg>
  <div class="a" style="left:18px;top:80px;width:66px;text-align:center;font-size:3.2px;font-weight:600;color:#8fb0e6">LOREM IPSUM DOLOR</div>
  <div class="a" style="left:89px;top:80px;width:66px;text-align:center;font-size:3.2px;font-weight:600;color:#8fb0e6">LOREM IPSUM DOLOR</div>
  <div class="a" style="left:160px;top:80px;width:66px;text-align:center;font-size:3.2px;font-weight:600;color:#8fb0e6">LOREM IPSUM DOLOR</div>
  <p class="a copy light" style="left:22px;top:87px;width:58px;text-align:center">“Lorem ipsum dolor sit amet, consectetur adipiscing elit. Phasellus sodales, ligula ultrices tempus ristique, tellus justo aliquam dui</p>
  <p class="a copy light" style="left:93px;top:87px;width:58px;text-align:center">“Lorem ipsum dolor sit amet, consectetur adipiscing elit. Phasellus sodales, ligula ultrices tempus ristique, tellus justo aliquam dui</p>
  <p class="a copy light" style="left:164px;top:87px;width:58px;text-align:center">“Lorem ipsum dolor sit amet, consectetur adipiscing elit. Phasellus sodales, ligula ultrices tempus ristique, tellus justo aliquam dui</p>
</section>

<section class="slide" style="left:331px;top:882px">
  <div class="photo ph-office" style="left:12px;top:12px;width:46px;height:40px" role="img" aria-label="Meeting room"></div>
  <div class="photo ph-warm" style="left:60px;top:12px;width:48px;height:45px" role="img" aria-label="Team at a table"></div>
  <div class="photo ph-warm" style="left:12px;top:54px;width:46px;height:45px" role="img" aria-label="Business people talking"></div>
  <div class="photo ph-office" style="left:60px;top:59px;width:48px;height:66px" role="img" aria-label="Celebrating colleague"></div>
  <div class="photo ph-office" style="left:12px;top:101px;width:46px;height:24px" role="img" aria-label="Person at a laptop"></div>
  <div class="a" style="left:124px;top:22px;font-size:6.4px;font-weight:500;color:var(--blue);line-height:1.35">Lorem ipsum dolor<br>sit amet, consectetur</div>
  <p class="a copy" style="left:124px;top:46px;width:106px">“Lorem ipsum dolor sit amet, consectetur adipiscing elit. Phasellus sodales, ligula ultrices tempus ristique, tellus justo aliquam dui, nec Lorem ipsum dolor sit amet, consectetur “Lorem ipsum dolor sit amet, consectetur adipiscing elit. Phasellus sodales, ligula ultrices tempus ristique, tellus justo aliquam dui, nec Lorem ipsum dolor sit amet, consectetur “Lorem ipsum dolor sit amet, consectetur adipiscing elit. Phasellus sodales, ligula ultrices tempus ristique, tellus justo aliquam dui, nec Lorem ipsum dolor sit amet, consectetur “Lorem ipsum dolor sit amet, consectetur adipiscing elit.</p>
</section>

<section class="slide" style="left:607px;top:882px">
  <div class="a heading" style="left:14px;top:13px;font-size:6px">Edit Title Here</div>
  <div class="photo ph-dusk" style="left:16px;top:28px;width:214px;height:64px" role="img" aria-label="City skyline at dusk with highway light trails"></div>
  <svg class="icon" style="left:20px;top:102px;width:13px;height:13px"><use href="#i-people"/></svg>
  <svg class="icon" style="left:130px;top:102px;width:13px;height:13px"><use href="#i-play"/></svg>
  <div class="a label" style="left:40px;top:102px">Lorem Ipsum</div><p class="a copy" style="left:40px;top:107px;width:72px">Lorem ipsum dolor sit amet, consectetur adipiscing elit, sed do eiusmod tempor incididunt ut labore et dolore magna aliqua. Ut enim ad minim</p>
  <div class="a label" style="left:150px;top:102px">Lorem Ipsum</div><p class="a copy" style="left:150px;top:107px;width:72px">Lorem ipsum dolor sit amet, consectetur adipiscing elit, sed do eiusmod tempor incididunt ut labore et dolore magna aliqua. Ut enim ad minim</p>
</section>

<section class="slide" style="left:885px;top:882px">
  <div class="photo ph-blue" style="left:0;top:0;width:244px;height:137px" role="img" aria-label="Looking up at skyscrapers, tinted blue"></div>
  <div class="a" style="left:70px;top:31px;width:104px;height:.6px;background:rgba(255,255,255,.6)"></div>
  <div class="a white-text" style="left:0;top:37px;width:244px;text-align:center;font-size:13px;font-weight:500">THANK YOU</div>
  <div class="a" style="left:70px;top:56px;width:104px;height:.6px;background:rgba(255,255,255,.6)"></div>
  <div class="a white-text" style="left:0;top:70px;width:244px;text-align:center;font-size:4.6px;font-weight:600">Harbourline Capital</div>
  <div class="a white-text" style="left:0;top:83px;width:244px;text-align:center;font-size:3.4px;font-weight:600;line-height:1.4">200 Meridian Ave,<br>Lakeview, CA 90210</div>
  <div class="a white-text" style="left:0;top:98px;width:244px;text-align:center;font-size:3.2px;font-weight:600">P: 555 010 2040 &nbsp;•&nbsp; www.harbourline.com</div>
</section>
</body>
</html>
```